Data Compass Plan- Brennal Insurance providing specialist Cyber and Liability Insurance

for Managed Technology Service Providers and their customer, we will use a letterhead that white labels insurer documents, which can be used in our physical letters as well as to be used within Email signatures.

Target Market(s)

Managed Technology Services Providers

Industry/Entity Type

Cyber Insurance

Requirements
Must have
• website, email address, contact phone numbers

```html
<!DOCTYPE html>
<html lang="en">
<head>
<meta charset="utf-8">
<title>Data Compass Plan – Letterhead</title>
<link href="https://fonts.googleapis.com/css2?family=Questrial&display=swap" rel="stylesheet">
<style>
  :root {
    --backdrop: #e6e6e6;
    --paper: #ffffff;
    --ink: #5a5a5a;
    --ink-soft: #666666;
    --brand-green: #4cbb58;
    --brand-grey: #58585a;
  }
  * { margin: 0; padding: 0; box-sizing: border-box; }
  html, body {
    width: 1024px;
    height: 1200px;
    overflow: hidden;
    background: var(--backdrop);
  }
  .letterhead {
    position: absolute;
    left: 122px;
    top: 49px;
    width: 780px;
    height: 1102px;
    background: var(--paper);
    font-family: "Questrial", "Century Gothic", sans-serif;
    color: var(--ink);
    overflow: hidden;
  }
  .brand-name {
    position: absolute;
    left: 31px;
    top: 48px;
    font-size: 27px;
    line-height: 1.2;
    letter-spacing: 0.5px;
    color: var(--ink);
    white-space: nowrap;
  }
  .header-rule {
    position: absolute;
    left: 0;
    top: 94px;
    width: 551px;
    height: 1px;
    background: var(--brand-green);
  }
  .contact-list {
    position: absolute;
    left: 556px;
    top: 42px;
    list-style: none;
  }
  .contact-item {
    display: flex;
    align-items: center;
    height: 20.5px;
    font-size: 12.5px;
    color: var(--ink-soft);
    white-space: nowrap;
  }
  .contact-icon {
    width: 12px;
    height: 12px;
    margin-right: 8px;
    flex: none;
  }
  .footer-band {
    position: absolute;
    left: 0;
    bottom: 0;
    width: 100%;
  }
  .footer-rule {
    height: 6px;
    background: var(--brand-grey);
  }
  .footer-gap {
    height: 5px;
    background: var(--paper);
  }
  .footer-fill {
    height: 44px;
    background: var(--brand-green);
  }
</style>
</head>
<body>
  <main class="letterhead">
    <div class="brand-name">Data Compass Plan</div>
    <div class="header-rule"></div>

    <ul class="contact-list">
      <li class="contact-item">
        <svg class="contact-icon" viewBox="0 0 12 12" aria-hidden="true">
          <circle cx="6" cy="6" r="6" fill="var(--brand-green)"/>
          <path d="M4 3.2c.3-.3.7-.2.9.1l.5.8c.1.3 0 .6-.2.8l-.3.2c.3.7.8 1.2 1.5 1.5l.2-.3c.2-.2.5-.3.8-.2l.8.5c.3.2.4.6.1.9l-.4.4c-.5.4-1.6.2-2.9-1.1S3.1 4.2 3.6 3.6z" fill="#fff"/>
        </svg>
        0123-555-018
      </li>
      <li class="contact-item">
        <svg class="contact-icon" viewBox="0 0 12 12" aria-hidden="true">
          <circle cx="6" cy="6" r="6" fill="var(--brand-green)"/>
          <rect x="3" y="4" width="6" height="4.2" rx="0.4" fill="#fff"/>
          <path d="M3.2 4.2 6 6.3l2.8-2.1" fill="none" stroke="var(--brand-green)" stroke-width="0.7"/>
        </svg>
        info@datacompassplan.com
      </li>
      <li class="contact-item">
        <svg class="contact-icon" viewBox="0 0 12 12" aria-hidden="true">
          <circle cx="6" cy="6" r="6" fill="var(--brand-green)"/>
          <g fill="none" stroke="#fff" stroke-width="0.6">
            <circle cx="6" cy="6" r="3.2"/>
            <ellipse cx="6" cy="6" rx="1.4" ry="3.2"/>
            <path d="M2.8 6h6.4M3.3 4.4h5.4M3.3 7.6h5.4"/>
          </g>
        </svg>
        www.datacompassplan.com
      </li>
    </ul>

    <div class="footer-band" aria-hidden="true">
      <div class="footer-rule"></div>
      <div class="footer-gap"></div>
      <div class="footer-fill"></div>
    </div>
  </main>
</body>
</html>
```